Pedal Wardens stationary
business card, letter head, powerpoint template
Creative Brief
Use same font as used in my logo
Tomas Lindqvo
Owner & Managing Director
Ekbackevägen 14 17452 Sundbyö
tomas@pedalwardens.cc
www.pedalwardens.cc
org.nr. 558213-4406
Business card and stationary design. We provide umpires & referees for teams/organizations.

```html
<!DOCTYPE html>
<html lang="en">
<head>
<meta charset="utf-8">
<title>Pedal Wardens – Business Card</title>
<link rel="stylesheet" href="https://fonts.googleapis.com/css2?family=Open+Sans:wght@300;400;700&display=swap">
<style>
  :root {
    --backdrop: #e9e7e4;
    --card: #ffffff;
    --ink: #3a3a3c;
    --ink-soft: #4a4a4c;
    --accent-dark: #3b3b3e;
  }
  * { margin: 0; padding: 0; box-sizing: border-box; }
  html, body {
    width: 1200px; height: 902px; overflow: hidden;
    background: var(--backdrop);
    font-family: "Open Sans", Arial, sans-serif;
  }
  .business-card {
    position: absolute; left: 100px; top: 161px;
    width: 1000px; height: 580px;
    background: var(--card);
    overflow: hidden;
    box-shadow: 0 6px 24px rgba(0,0,0,0.18);
  }
  .brand-disc {
    position: absolute; left: 0; top: 0;
    width: 1000px; height: 580px;
  }
  .wordmark {
    position: absolute; left: 58px; top: 138px;
    font-weight: 300; font-size: 38px;
    letter-spacing: 0.2em; text-transform: uppercase;
    color: var(--ink); white-space: nowrap;
  }
  .holder {
    position: absolute; left: 58px; top: 306px;
    color: var(--ink);
  }
  .holder-name { font-weight: 700; font-size: 23px; line-height: 1.25; }
  .holder-role { font-weight: 400; font-size: 17px; line-height: 1.4; color: var(--ink-soft); }
  .contact-list {
    position: absolute; left: 58px; top: 412px;
    list-style: none;
  }
  .contact-item {
    display: flex; align-items: center; gap: 10px;
    font-size: 19px; color: var(--ink); line-height: 1; height: 32px;
  }
  .contact-icon { width: 20px; height: 20px; flex: none; }
</style>
</head>
<body>
  <div class="business-card">
    <svg class="brand-disc" viewBox="0 0 1000 580" aria-hidden="true">
      <circle cx="840" cy="300" r="330" fill="var(--accent-dark)"/>
    </svg>

    <div class="wordmark">Pedal Wardens</div>

    <div class="holder">
      <div class="holder-name">Tomas Lindqvo</div>
      <div class="holder-role">Owner &amp; Managing Director</div>
    </div>

    <ul class="contact-list">
      <li class="contact-item">
        <svg class="contact-icon" viewBox="0 0 20 20" aria-hidden="true">
          <circle cx="10" cy="10" r="10" fill="var(--ink)"/>
          <path d="M10 4.5a3.5 3.5 0 0 0-3.5 3.5c0 2.6 3.5 7 3.5 7s3.5-4.4 3.5-7A3.5 3.5 0 0 0 10 4.5z" fill="#fff"/>
          <circle cx="10" cy="8" r="1.3" fill="var(--ink)"/>
        </svg>
        Ekbackevägen 14 17452 Sundbyö
      </li>
      <li class="contact-item">
        <svg class="contact-icon" viewBox="0 0 20 20" aria-hidden="true">
          <circle cx="10" cy="10" r="10" fill="var(--ink)"/>
          <rect x="5" y="6.5" width="10" height="7" rx="1" fill="#fff"/>
          <path d="M5.3 7l4.7 3.6L14.7 7" fill="none" stroke="var(--ink)" stroke-width="1"/>
        </svg>
        tomas@pedalwardens.cc
      </li>
      <li class="contact-item">
        <svg class="contact-icon" viewBox="0 0 20 20" aria-hidden="true">
          <circle cx="10" cy="10" r="10" fill="var(--ink)"/>
          <circle cx="10" cy="10" r="5" fill="none" stroke="#fff" stroke-width="1.2"/>
          <ellipse cx="10" cy="10" rx="2.2" ry="5" fill="none" stroke="#fff" stroke-width="1"/>
          <path d="M5 10h10" stroke="#fff" stroke-width="1"/>
        </svg>
        www.pedalwardens.cc
      </li>
    </ul>
  </div>
</body>
</html>
```